Fine Dining Restaurant needs Harbour Stakes Day Flyer

We need a flyer to promote Harbour Stakes day at our restaurant in Port Douglas, QLD.
Details:
6th November 2018
It's a ticketed event, including a fine-dining 4 course lunch, with 3 hour drinks package, to include sweeps & prizes.
Starts 11:30 - 14:30.
Ticket price: $160 with $5 from each ticket going to Tails & Whiskers
Cash bar also available.
Address: 47 Copperleaf Lane, Port Douglas
Contact: 0740553819 or bookings@lorindas.net.au
*Big screen TV's
*Sweeps
*Best Dressed prizes and more...
*Glass of sparkling wine on arrival
*Discount for tables of 8 or more...
Design: we'd like to see a really elegant design for the flyer, with the use of tropical florals, utilising whites and some burnt orange colours if suitable.
Size: To be printed on A4

```html
<!DOCTYPE html>
<html lang="en">
<head>
<meta charset="utf-8">
<title>Harbour Stakes Day at Lorinda's</title>
<link href="https://fonts.googleapis.com/css2?family=Great+Vibes&family=Open+Sans:wght@300;400;600;700&display=swap" rel="stylesheet">
<style>
  :root {
    --backdrop: #1b1b1b;
    --paper: #ffffff;
    --burnt-orange: #e2411e;
    --deep-orange: #c8341a;
    --ink: #222222;
    --soft-sky: #e9f1f6;
    --photo-dark: #3a2a22;
    --photo-warm: #b4532e;
  }
  * { box-sizing: border-box; margin: 0; padding: 0; }
  html, body {
    width: 1200px; height: 800px; overflow: hidden;
    background: var(--backdrop);
    font-family: "Open Sans", sans-serif;
  }
  .flyer {
    position: absolute;
    left: 296px; top: 7px;
    width: 608px; height: 785px;
    background: var(--paper);
    overflow: hidden;
  }
  .flyer__art { position: absolute; inset: 0; }
  .brand {
    position: absolute; left: 452px; top: 20px;
    width: 135px; height: 82px;
    background: var(--paper);
    display: flex; align-items: center; justify-content: center;
    font-family: "Open Sans", sans-serif; font-weight: 700;
    font-size: 17px; letter-spacing: 0.5px; color: var(--ink);
  }
  .badge {
    position: absolute; left: 285px; top: 320px;
    width: 250px; height: 250px;
    display: flex; flex-direction: column; align-items: center; justify-content: center;
    text-align: center;
  }
  .badge__title {
    font-family: "Great Vibes", cursive;
    font-weight: 400;
    color: var(--burnt-orange);
    font-size: 46px; line-height: 0.95;
    margin-top: 10px;
  }
  .badge__sub {
    margin-top: 10px;
    font-size: 13px; line-height: 1.45; color: var(--ink);
  }
  .intro {
    position: absolute; left: 22px; top: 466px;
    font-size: 10px; line-height: 1.4; color: var(--ink);
  }
  .price {
    position: absolute; left: 22px; top: 527px;
    display: flex; align-items: center; gap: 8px;
    color: var(--burnt-orange);
  }
  .price__label { font-size: 18px; font-weight: 300; line-height: 1.15; }
  .price__amount { font-size: 48px; font-weight: 300; line-height: 1; }
  .price__note {
    position: absolute; left: 22px; top: 577px;
    font-size: 13px; line-height: 1.4; color: var(--ink);
  }
  .cash-bar {
    position: absolute; left: 22px; top: 628px;
    font-size: 13px; font-weight: 700; color: var(--burnt-orange);
  }
  .perks {
    position: absolute; left: 22px; top: 668px;
    list-style: none; font-size: 14px; line-height: 20.5px; color: var(--ink);
    white-space: nowrap;
  }
  .perks li { display: flex; align-items: center; gap: 5px; }
  .perks svg { width: 12px; height: 12px; flex: none; }
  .details {
    position: absolute; left: 304px; top: 668px;
    font-size: 13px; line-height: 20.5px; color: var(--ink);
    white-space: nowrap;
  }
  .details b { font-weight: 700; }
</style>
</head>
<body>
  <main class="flyer">
    <svg class="flyer__art" viewBox="0 0 608 785" width="608" height="785">
      <defs>
        <linearGradient id="venueTones" x1="0" y1="0" x2="0.6" y2="1">
          <stop offset="0" stop-color="#4a3a33"/>
          <stop offset="0.55" stop-color="var(--photo-dark)"/>
          <stop offset="1" stop-color="var(--photo-warm)"/>
        </linearGradient>
        <radialGradient id="wreathTones" cx="0.5" cy="0.5" r="0.5">
          <stop offset="0.68" stop-color="#f07a3a"/>
          <stop offset="0.85" stop-color="var(--burnt-orange)"/>
          <stop offset="1" stop-color="#f4b27a" stop-opacity="0.2"/>
        </radialGradient>
      </defs>
      <polygon class="venue-photo" role="img" aria-label="Photo of the restaurant's tropical garden terrace with paper lanterns and orange cushioned lounges"
        points="0,0 608,0 608,215 420,395 235,432 0,385" fill="url(#venueTones)"/>
      <polygon class="accent-band" points="0,385 235,432 235,438 0,400" fill="var(--burnt-orange)"/>
      <polygon class="accent-band" points="608,215 608,235 520,320 505,320" fill="var(--burnt-orange)"/>
      <circle class="wreath" role="img" aria-label="Wreath of tropical flowers and leaves in burnt orange tones"
        cx="410" cy="445" r="188" fill="url(#wreathTones)"/>
      <circle class="badge-ring" cx="410" cy="445" r="132" fill="var(--paper)"/>
      <circle class="badge-ring" cx="410" cy="445" r="127" fill="none" stroke="var(--burnt-orange)" stroke-width="2"/>
      <circle class="badge-fill" cx="410" cy="445" r="123" fill="var(--soft-sky)"/>
    </svg>

    <div class="brand">LORINDA'S</div>

    <div class="badge">
      <h1 class="badge__title">Harbour<br>Stakes Day</h1>
      <p class="badge__sub">at our restaurant in<br>Port Douglas, QLD.</p>
    </div>

    <p class="intro">It's a ticketed event,<br>including a fine-dining 4 course lunch,<br>with 3 hour drinks package,<br>to include sweeps &amp; prizes.</p>

    <div class="price">
      <span class="price__label">TICKET<br>PRICE:</span>
      <span class="price__amount">$160</span>
    </div>
    <p class="price__note">with $5 from each ticket<br>going to Tails &amp; Whiskers</p>

    <p class="cash-bar">CASH BAR ALSO AVAILABLE.</p>

    <ul class="perks">
      <li><svg viewBox="0 0 12 12"><polygon points="0,0 12,6 0,12" fill="var(--burnt-orange)"/></svg>Big screen TV's</li>
      <li><svg viewBox="0 0 12 12"><polygon points="0,0 12,6 0,12" fill="var(--burnt-orange)"/></svg>Sweeps</li>
      <li><svg viewBox="0 0 12 12"><polygon points="0,0 12,6 0,12" fill="var(--burnt-orange)"/></svg>Best Dressed prizes and more...</li>
      <li><svg viewBox="0 0 12 12"><polygon points="0,0 12,6 0,12" fill="var(--burnt-orange)"/></svg>Glass of sparkling wine on arrival</li>
      <li><svg viewBox="0 0 12 12"><polygon points="0,0 12,6 0,12" fill="var(--burnt-orange)"/></svg>Discount for tables of 8 or more...</li>
    </ul>

    <div class="details">
      <p><b>DATE:</b> 6th November 2018</p>
      <p><b>STARTS</b> 11:30 - 14:30.</p>
      <p><b>ADDRESS:</b> 47 Copperleaf Lane, Port Douglas</p>
      <p><b>CONTACT:</b> 0740553819</p>
      <p><b>or</b> bookings@lorindas.net.au</p>
    </div>
  </main>
</body>
</html>
```